Business Card Design

I need a Business Card that will catch the attention that will not get thrown in a Drawer. I have 23 companies I use for Auto, Home, Life, and Business Insurance. I make sure that people have the best coverage for the $ spent.

Industry/Entity Type

Business

Contact Information for Business Card

Dorlin Insurance Agency, Inc., Marcus Helgren, 4375 West Tamber Lane Harlow Falls, Kelmont 45192 555-281-7496, www.dorlinagency.example, Facebook, LinkedIn, Google+

```html
<!DOCTYPE html>
<html lang="en">
<head>
<meta charset="utf-8">
<title>Dorlin Insurance Agency – Business Card</title>
<link rel="stylesheet" href="https://fonts.googleapis.com/css2?family=Source+Sans+3:wght@400;600&display=swap">
<style>
  :root {
    --backdrop: #d8d8d8;
    --card-white: #f4f4f2;
    --green-strong: #8cc63f;
    --green-mid: #b6dc80;
    --green-pale: #d2eab0;
    --rule-dark: #2b2b2b;
    --rule-grey: #9a9a9a;
    --ink: #1f2a14;
    --icon-fill: #9bcf5a;
  }
  * { box-sizing: border-box; margin: 0; padding: 0; }
  html, body { width: 1200px; height: 750px; overflow: hidden; }
  body {
    background: var(--backdrop);
    font-family: "Source Sans 3", "Myriad Pro", sans-serif;
    color: var(--ink);
    position: relative;
  }
  .card {
    position: absolute;
    background: var(--card-white);
    border-radius: 16px;
    overflow: hidden;
    box-shadow: 0 2px 6px rgba(0,0,0,.18);
  }
  .band { position: absolute; left: 0; right: 0; }
  .company-name { font-weight: 600; letter-spacing: .2px; white-space: nowrap; }
  .person-name { font-weight: 600; white-space: nowrap; }
  .person-name .initial { font-size: 1.3em; }
  .contact-list { list-style: none; font-size: 13px; line-height: 20px; white-space: nowrap; }
  .icon-row { display: flex; gap: 6px; }
  .icon { width: 18px; height: 18px; display: block; }
  .rule-dark { background: var(--rule-dark); }
  .rule-grey { background: var(--rule-grey); }
  .address { font-size: 12px; white-space: nowrap; }

  /* Landscape side */
  .card-front { left: 70px; top: 215px; width: 560px; height: 320px; }
  .card-front .band-header { top: 0; height: 58px; background: var(--green-mid);
    display: flex; align-items: center; justify-content: flex-end; padding-right: 110px; }
  .card-front .band-header .company-name { font-size: 20px; }
  .card-front .band-contact { top: 74px; height: 48px; background: var(--green-pale); }
  .card-front .contact-block { position: absolute; left: 288px; top: 78px; display: flex; gap: 8px; align-items: center; }
  .card-front .icon-col { display: flex; flex-direction: column; gap: 3px; }
  .card-front .name-box { position: absolute; left: 58px; top: 150px; width: 200px; height: 40px;
    background: var(--green-pale); display: flex; align-items: center; justify-content: center; font-size: 16px; }
  .card-front .rule-dark { top: 262px; height: 3px; }
  .card-front .rule-grey { top: 267px; height: 2px; }
  .card-front .band-footer { top: 272px; bottom: 0; background: var(--green-strong);
    display: flex; align-items: center; justify-content: center; }

  /* Portrait side */
  .card-back { left: 800px; top: 95px; width: 320px; height: 560px; }
  .card-back .band-header { top: 0; height: 64px; background: var(--green-mid);
    display: flex; align-items: center; justify-content: center; }
  .card-back .band-header .company-name { font-size: 19px; }
  .card-back .band-name { top: 100px; height: 92px; background: var(--green-pale);
    display: flex; align-items: center; justify-content: center; font-size: 18px; }
  .card-back .icon-row { position: absolute; left: 40px; top: 214px; }
  .card-back .band-contact { top: 238px; height: 62px; background: var(--green-pale);
    padding: 10px 0 0 40px; }
  .card-back .rule-dark { top: 438px; height: 4px; }
  .card-back .rule-grey { top: 444px; height: 2px; }
  .card-back .band-footer { top: 448px; bottom: 0; background: var(--green-strong);
    padding: 18px 0 0 24px; }
  .card-back .address { font-size: 14px; line-height: 19px; }
</style>
</head>
<body>

<section class="card card-front" aria-label="Business card, landscape side">
  <div class="band band-header"><span class="company-name">Dorlin Insurance Agency Inc</span></div>
  <div class="band band-contact"></div>
  <div class="contact-block">
    <div class="icon-col">
      <svg class="icon" viewBox="0 0 18 18" aria-label="Phone"><circle cx="9" cy="9" r="9" fill="var(--icon-fill)"/><path d="M6 5h2l1 2.5-1.2.8a5 5 0 0 0 2 2l.8-1.2L13 10v2c0 .6-.5 1-1 1A7 7 0 0 1 5 6c0-.6.4-1 1-1z" fill="#fff"/></svg>
      <svg class="icon" viewBox="0 0 18 18" aria-label="Website"><circle cx="9" cy="9" r="9" fill="var(--icon-fill)"/><circle cx="9" cy="9" r="4.5" fill="none" stroke="#fff" stroke-width="1.2"/><path d="M4.5 9h9M9 4.5c-2 2.5-2 6.5 0 9M9 4.5c2 2.5 2 6.5 0 9" fill="none" stroke="#fff" stroke-width="1"/></svg>
    </div>
    <ul class="contact-list">
      <li>555-281-7496</li>
      <li>www.dorlinagency.example</li>
    </ul>
  </div>
  <div class="name-box person-name"><span><span class="initial">M</span>arcus <span class="initial">H</span>elgren</span></div>
  <div class="band rule-dark"></div>
  <div class="band rule-grey"></div>
  <div class="band band-footer"><p class="address">Dorlin Insurance Agency: 4375 West Tamber Lane Harlow Falls, Kelmont 45192</p></div>
</section>

<section class="card card-back" aria-label="Business card, portrait side">
  <div class="band band-header"><span class="company-name">Dorlin Insurance Agency Inc</span></div>
  <div class="band band-name person-name"><span><span class="initial">M</span>arcus <span class="initial">H</span>elgren</span></div>
  <div class="icon-row">
    <svg class="icon" viewBox="0 0 18 18" aria-label="Phone"><circle cx="9" cy="9" r="9" fill="var(--icon-fill)"/><path d="M6 5h2l1 2.5-1.2.8a5 5 0 0 0 2 2l.8-1.2L13 10v2c0 .6-.5 1-1 1A7 7 0 0 1 5 6c0-.6.4-1 1-1z" fill="#fff"/></svg>
    <svg class="icon" viewBox="0 0 18 18" aria-label="Website"><circle cx="9" cy="9" r="9" fill="var(--icon-fill)"/><circle cx="9" cy="9" r="4.5" fill="none" stroke="#fff" stroke-width="1.2"/><path d="M4.5 9h9M9 4.5c-2 2.5-2 6.5 0 9M9 4.5c2 2.5 2 6.5 0 9" fill="none" stroke="#fff" stroke-width="1"/></svg>
  </div>
  <div class="band band-contact">
    <ul class="contact-list">
      <li>555-281-7496</li>
      <li>www.dorlinagency.example</li>
    </ul>
  </div>
  <div class="band rule-dark"></div>
  <div class="band rule-grey"></div>
  <div class="band band-footer">
    <p class="address">Dorlin Insurance Agency<br>4375 West Tamber Lane Harlow Falls<br>Kelmont 45192</p>
  </div>
</section>

</body>
</html>
```